Web Design Project

To develop a web based Council Meeting Support system which includes 2 major components for each Council member:
1. Allow a council member to Vote on a motion during a council session
2. Allow a council member to flag notify the Chair their intention to speak on a motion
The application will have 3 separate interfaces:
Chair interface: Allows the Chair of the session to review voting and manage the speaker queue
Council interface: Allows each council member to vote on each motion and add flag their intention to speak for or against a motion
Admin interface: Allows administrators to initiate a session and import details on all meeting participants
We will begin by designing the Council Interface. (An example wireframe is attached) This council interface will give members the ability to request to speak, vote, view voting results and viewing the current motion number.
*** 4 Designs will be required overall. One for each interface and a login page ***
Needs to be designed so that it works well on an Tavlo or any tablet device.
Update: Looking for a brighter design, not a dark grey one. The blue colour from qarvel.example would be good.
- Request to Speak
Voting
Vote Results
Current Motion Number

```html
<!DOCTYPE html>
<html lang="en">
<head>
<meta charset="utf-8">
<title>Council Interface</title>
<link rel="stylesheet" href="https://fonts.googleapis.com/css2?family=Crimson+Text&family=Source+Sans+3:wght@400;600&family=Arimo&display=swap">
<style>
  :root {
    --navy: #0b3a6c;
    --teal: #0f6d9f;
    --ink: #1f3d6b;
    --text: #16365f;
    --frame: #dbe2ea;
    --panel-head: #e2ecf3;
    --panel-body: #f3f7fa;
    --divider: #e0e8ef;
    --muted: #7d8ba0;
    --white: #ffffff;
  }
  * { box-sizing: border-box; margin: 0; padding: 0; }
  html, body { width: 1200px; height: 1181px; overflow: hidden; background: var(--white); }
  body { position: relative; font-family: "Source Sans 3", sans-serif; color: var(--text); }

  .page {
    position: absolute; left: 32px; top: 14px; width: 1157px; height: 1200px;
    background: var(--white); box-shadow: 0 0 4px rgba(0,0,0,.18);
  }
  .abs { position: absolute; }

  .brand-name { left: 61px; top: 64px; font-family: "Crimson Text", serif; font-size: 29px; color: var(--ink); line-height: 1; }
  .brand-slogan { left: 131px; top: 100px; font-size: 15px; color: var(--ink); }

  .nav { left: 581px; top: 86px; display: flex; align-items: center; height: 42px; font-family: "Arimo", sans-serif; font-size: 15px; color: var(--ink); }
  .nav-item { padding: 0 24px; line-height: 18px; border-left: 1px solid #b8c4d2; }
  .nav-item.active { background: var(--navy); color: var(--white); border-radius: 21px; height: 42px; line-height: 42px; padding: 0 25px; border: 0; margin-right: 0; }
  .nav-item.first { border-left: 0; padding-left: 26px; }

  .hero { left: 47px; top: 150px; width: 1109px; height: 440px; border: 1px solid var(--frame); overflow: hidden; }
  .hero-photo { position: absolute; inset: 0; background: linear-gradient(100deg, #7a93b3 0%, #b9cde2 30%, #dce8f3 55%, #eef3f8 80%, #d7e4f0 100%); }
  .speak-box { left: 656px; top: 116px; width: 394px; height: 236px; background: rgba(255,255,255,.72); border: 1px solid rgba(255,255,255,.9); border-radius: 6px; }
  .speak-title { left: 35px; top: 25px; font-size: 18px; font-weight: 600; color: var(--navy); }

  .btn { position: absolute; display: block; height: 44px; line-height: 44px; text-align: center; color: var(--white); background: var(--navy); border-radius: 5px; font-size: 21px; }
  .btn.teal { background: var(--teal); }
  .speak-box .btn { left: 61px; width: 249px; font-size: 20px; }

  .lower { left: 47px; top: 600px; width: 1109px; height: 509px; border: 1px solid var(--frame); }
  .voting-title { left: 38px; top: 30px; font-size: 20px; color: #111; }
  .lower .voting-btn { left: 35px; width: 226px; }

  .results { left: 318px; top: 11px; width: 777px; height: 478px; background: var(--panel-body); }
  .results-head { position: absolute; left: 0; top: 0; width: 100%; height: 48px; background: var(--panel-head); font-size: 19px; font-weight: 600; color: var(--navy); line-height: 48px; padding-left: 27px; }
  .col { position: absolute; top: 48px; height: 430px; }
  .col + .col { border-left: 1px solid var(--divider); }
  .col h3 { position: absolute; top: 22px; font-size: 17px; font-weight: 600; color: var(--navy); }
  .col ul { position: absolute; top: 56px; list-style: none; }
  .col li { height: 29.3px; font-size: 14.5px; color: var(--text); position: relative; padding-left: 17px; }
  .col li::before { content: ""; position: absolute; left: 1px; top: 5px; border-left: 5px solid var(--navy); border-top: 4px solid transparent; border-bottom: 4px solid transparent; }

  .footer { left: 61px; top: 1128px; font-size: 13px; color: var(--muted); }
</style>
</head>
<body>
<div class="page"></div>

<div class="abs brand-name">Company Name</div>
<div class="abs brand-slogan">slogan goes here</div>

<nav class="abs nav">
  <span class="nav-item active">MAIN</span>
  <span class="nav-item first">COMPANY</span>
  <span class="nav-item">SERVICES</span>
  <span class="nav-item">MEMBER</span>
  <span class="nav-item">CONTACT</span>
</nav>

<section class="abs hero">
  <div class="hero-photo" role="img" aria-label="Photo of two council members looking upward against a bright cloudy sky"></div>
  <div class="abs speak-box">
    <div class="abs speak-title">I WOULD LIKE TO SPEAK:</div>
    <span class="btn" style="top:59px">FOR MOTION</span>
    <span class="btn" style="top:111px">AGAINST MOTION</span>
    <span class="btn teal" style="top:164px;font-size:18px">REMOVE FORM QUEUE</span>
  </div>
</section>

<section class="abs lower">
  <div class="abs voting-title">VOTING</div>
  <span class="btn voting-btn" style="top:79px">FOR</span>
  <span class="btn voting-btn" style="top:132px">AGAINST</span>
  <span class="btn teal voting-btn" style="top:184px">ABSTAIN</span>

  <div class="abs results">
    <div class="results-head">VOTE RESULTS</div>
    <div class="col" style="left:0;width:211px">
      <h3 style="left:68px">FOR</h3>
      <ul style="left:67px">
        <li>A. Marlowe</li><li>S.Velden</li><li>P. Corrigan</li><li>I.Dunmore</li><li>T. Halvey</li>
        <li>R.A. Kinsell</li><li>S.K Tarrow</li><li>S. Brenna</li><li>L.Ostrand</li><li>B. Varlen.</li>
      </ul>
    </div>
    <div class="col" style="left:211px;width:199px">
      <h3 style="left:56px">AGAINST</h3>
      <ul style="left:55px">
        <li>J.D. Pellow</li><li>S. Quarry</li><li>D.Menard</li><li>D. Fenwick</li><li>B. Laskin</li><li>R.J Tamsey</li>
        <li>R. Orwin</li><li>W. Delacey</li><li>M. Hale Storey</li><li>S. Wick</li><li>C.D Ashby</li><li>T. Norland</li>
      </ul>
    </div>
    <div class="col" style="left:410px;width:367px">
      <h3 style="left:47px">ABSTAIN</h3>
      <ul style="left:46px">
        <li>R.K Pemberlow</li><li>M. Treve</li><li>C. Barrow</li><li>M. Colm</li><li>R. Hartley</li>
      </ul>
    </div>
  </div>
</section>

<div class="abs footer">© 2012 Company Name &nbsp;|&nbsp; All right reserved</div>
</body>
</html>
```